Design einer Frühjahrsbroschüre für Immobilienmakler
Zielgruppe
Wir sind Immobilienmakler und möchten eine neue Frühjahrsbroschüre verteilen lassen.
Wir haben über Entwurfsmarkt schon mehrere Projekte gemacht und waren immer zufrieden.
Unsere Zielgruppe sind Immobilienverkäufer.
Aufgabenstellung
Der Flyer soll die Größe haben DinA3 auf DinA4 gefaltet. Somit sind 4 DinA4 Seiten zu gestallten.
Bei Papier im Fluss soll gedruckt werden. https://www.papier-im-fluss.de/faltblatt-gefalzt-auf-din-a4-4seiter.html#content-view
1. Seite: Frühlingshaft und ansprechende Aufmachung. Harmonische Farben. Ein Slogan.
Frühjahrsaktion: Verkäufer erhält nach Verkauf als Dankeschön für den Auftrag und sein Vertrauen in uns einen neuen Kochwerk KX4 oder 1000€ in bar.
2. Immobilienverkauf in Coronazeiten.
Warum Verkaufen mit Nord-Immobilien Kaltenbach
3. Aktuelle Immobilienangebote
4. Wir suchen für unsere Kunden
Im Anhang sind andere Flyer/Broschüren die uns seither gut gefallen haben.

```html
<!DOCTYPE html>
<html lang="de">
<head>
<meta charset="utf-8">
<title>Frühjahrsbroschüre – Innenseiten</title>
<link href="https://fonts.googleapis.com/css2?family=Figtree:wght@400;500;700;800;900&display=swap" rel="stylesheet">
<style>
:root{
  --navy:#1f2a7a;
  --gold:#b8963e;
  --gold-band:#b99540;
  --white:#ffffff;
  --ink:#1f2a7a;
}
*{box-sizing:border-box;margin:0;padding:0}
html,body{width:1200px;height:849px;overflow:hidden;background:var(--white)}
body{font-family:"Figtree",sans-serif;color:var(--ink);font-size:9.4px;line-height:12.3px}
.spread{position:relative;width:1200px;height:849px}
.abs{position:absolute}
.mark{position:absolute;width:18px;height:18px;border-radius:50%;background:var(--gold)}
.section-title{position:absolute;font-weight:800;font-size:12.5px;line-height:15px;letter-spacing:.6px;text-transform:uppercase;color:var(--navy)}
.section-title .light{font-weight:400}
b,.strong{font-weight:800}
.copy p{margin-bottom:12.3px}
.search-box{position:absolute;border:2px solid var(--navy);padding:12px 12px 8px 13px;font-size:9.4px;line-height:12.3px}
.search-box h4{color:var(--gold);font-weight:800;font-size:9.4px}
.promise{position:absolute;left:0;top:708px;width:600px;height:124px;background:var(--gold-band);color:var(--white)}
.promise .col{position:absolute;top:17px;font-size:10.4px;line-height:12.8px}
.promise h5{color:var(--navy);font-weight:900;font-size:10.4px;letter-spacing:.5px;text-transform:uppercase}
.listing-frame{position:absolute;border:2px solid var(--gold)}
.photo{position:absolute}
.listing-text{position:absolute;font-size:9.4px;line-height:12.4px}
.listing-text h3{font-weight:800;font-size:9.4px}
.listing-text p{margin-bottom:12.4px}
</style>
</head>
<body>
<main class="spread">

  <!-- Page: Corona -->
  <span class="mark" style="left:280px;top:21px"></span>
  <h2 class="section-title" style="left:218px;top:70px">Immobilienverkauf in<br>Zeiten von Corona –<br><span class="light">digital und persönlich</span></h2>

  <div class="copy abs" style="left:36px;top:147px;width:264px">
    <p>Sie fragen sich – wie kann man den <b>Immobilienverkauf</b> mit den aktuellen <b>Corona-Vorschriften</b> vereinbaren? Wir beraten Sie gerne per Telefon oder Videokonferenz.</p>
    <p>Ist Ihnen eine <b>persönliche Beratung</b> doch lieber, dann machen wir auch dies möglich – mit Einhaltung des Mindestabstand von 1,50 m, mit Mundschutz und Handschuhen.</p>
    <p>Der Fototermin findet selbstverständlich auch unter Einhaltung der <b>Hygienemaßnahmen</b> statt. Wir bewerben Ihre Immobilie auf Portalen wie <b>Wohnportal24, Marktplatz Lokal, Nachbarnetz</b> und auf</p>
  </div>
  <div class="copy abs" style="left:310px;top:147px;width:266px">
    <p>unserer Homepage. Darüber hinaus ermitteln wir passende Kaufinteressenten aus unserer Datenbank.</p>
    <p>Um Ihre Immobilie auch in diesen Zeiten <b>erfolgreich zu verkaufen,</b> haben wir auch für Ihre Kaufinteressenten digitale Lösungen geschaffen. Sollte ein Vor-Ort-Termin (mit max. 2 Personen) nicht möglich sein, besteht die Möglichkeit, Ihre Immobilie in Videokonferenzen und Video-Besichtigungstouren zu präsentieren.</p>
    <p><b>Käufer und Kaufpreis passen für Sie?</b><br>Dann kümmern wir uns um den Kaufvertrag und den Notartermin, um den Verkauf rechtssicher abzuschließen.</p>
  </div>

  <!-- Page: Search requests -->
  <span class="mark" style="left:280px;top:348px"></span>
  <h2 class="section-title" style="left:237px;top:398px">Wir suchen für<br>unsere Kunden</h2>

  <div class="search-box" style="left:403px;top:418px;width:156px;height:88px">
    <h4>Für eine Mutter mit Kind:</h4>Eine 3-4 Zimmerwohnung in Gaildorf und Umgebung, <b>Kaufpreis bis ca. 280.000€</b>
  </div>
  <div class="search-box" style="left:37px;top:458px;width:158px;height:88px">
    <h4>Für 3 Geschwister:</h4>Ein 3 Familienhaus in Gaildorf, Unterrot, Fichtenberg, <b>Kaufpreis bis 500.000€</b>
  </div>
  <div class="search-box" style="left:220px;top:458px;width:161px;height:88px">
    <h4>Für eine kleine Familie:</h4>Ein Bauplatz in Gaildorf und Umgebung oder ein EFH mit Garten, <b>Kaufpreis bis ca. 450.000€</b>
  </div>
  <div class="search-box" style="left:403px;top:528px;width:156px;height:130px">
    <h4>Für einen Kapitalanleger:</h4>Renovierungsbedürftige Wohnungen oder Häuser, MFH im großen Umkreis von 60 Km um Gaildorf (z.B. Schwäbisch Hall, Gaildorf, Backnang, Winnenden, Stuttgart, Crailheim), <b>Kaufpreis nicht begrenzt</b>
  </div>
  <div class="search-box" style="left:37px;top:567px;width:158px;height:92px">
    <h4>Für ein Ehepaar:</h4>Eine großzügige Wohnung im Umkreis von SHA, <b>Kaufpreis bis ca. 350.000€</b>
  </div>
  <div class="search-box" style="left:220px;top:567px;width:161px;height:92px">
    <h4>Für 2 Familien:</h4>Ein 2 Generationenhaus in ruhiger Randlage mit Garten Zwischen Gschwend und Backnang, <b>Kaufpreis bis 600.000€</b>
  </div>

  <!-- Promise band -->
  <section class="promise">
    <div class="col" style="left:36px;width:135px">
      <h5>Warum mit<br>Nord-Immobilien<br>verkaufen?</h5><br>
      <h5>Unser Versprechen:</h5>100 % Maklerservice,<br>0 % Provisionsschmerz
    </div>
    <div class="col" style="left:180px;width:105px">
      <h5>Erfahrene<br>Makler</h5>Wir kommen aus der Region und kennen den lokalen Immobilienmarkt seit Jahren.
    </div>
    <div class="col" style="left:292px;width:145px">
      <h5>Volle Service-<br>leistung</h5>Ihr lokaler Makler steht Ihnen bei jedem Schritt des Verkaufs zur Seite: von der Bewertung und Bewerbung bis zur Schlüsselübergabe.
    </div>
    <div class="col" style="left:447px;width:120px">
      <h5>Keine Verkaufs-<br>provision</h5>Der gesamte Service ist bei uns für Verkäufer kostenfrei.
    </div>
  </section>

  <!-- Page: Listings -->
  <span class="mark" style="left:877px;top:15px"></span>
  <h2 class="section-title" style="left:836px;top:65px">Aktuelle Immo-<br>bilien-Angebote</h2>

  <div class="listing-frame" style="left:812px;top:118px;width:353px;height:165px"></div>
  <div class="photo" role="img" aria-label="Luftaufnahme einer Wohnsiedlung mit Mehrfamilienhäusern" style="left:636px;top:128px;width:212px;height:144px;background:linear-gradient(180deg,#cfdbe8 0%,#b9c7b4 28%,#8f8a78 60%,#6e7a52 100%)"></div>
  <div class="listing-text" style="left:872px;top:145px;width:140px">
    <h3>Herrliche Aussicht<br>aus dem 11. Stock</h3>
    <p>3,5 Zimmer Wohnung<br>in Backnang<br>71522 Backnang</p>
    Kaufpreis: 299.000,00€<br>Fläche: 98,61m²<br>Zimmer: 3,5
  </div>
  <div class="listing-text" style="left:1022px;top:145px;width:140px">
    <p>Energieausweis: C</p><p>Energieausweistyp:<br>Verbrauchsausweis</p>Energiebedarf/<br>Energieverbrauch:<br>94 kWh/(m²*a)
  </div>

  <div class="listing-frame" style="left:637px;top:300px;width:353px;height:166px"></div>
  <div class="photo" role="img" aria-label="Lange Werkstatthalle mit Holzfassade und Rasenfläche" style="left:953px;top:312px;width:212px;height:143px;background:linear-gradient(180deg,#c9dcef 0%,#d8e3ea 30%,#6b5a48 45%,#9aa0a0 65%,#6f9a3c 82%,#4f7a2a 100%)"></div>
  <div class="listing-text" style="left:668px;top:332px;width:145px">
    <h3>Halle/Werkstatt mit<br>Photovoltaikanlage</h3>
    <p>Wohnbebauung möglich<br>74405 Gaildorf</p>
    Kaufpreis: 398.000,00€<br>Fläche: 785,00m²<br>Grundstück: 1.466,00m²<br>Zimmer: 5
  </div>
  <div class="listing-text" style="left:818px;top:332px;width:130px">
    Energieausweis /<br>-ausweistyp &amp;<br>Energiebedarf /<br>-verbrauch liegt bei<br>Besichtigung vor
  </div>

  <div class="listing-frame" style="left:812px;top:486px;width:353px;height:165px"></div>
  <div class="photo" role="img" aria-label="Einfamilienhaus mit Solardach und Garten" style="left:636px;top:497px;width:212px;height:143px;background:linear-gradient(180deg,#3a7fd0 0%,#7fb0e4 35%,#a08a6c 55%,#7a9a4a 75%,#56803a 100%)"></div>
  <div class="listing-text" style="left:872px;top:510px;width:145px">
    <h3>Schönes großes Haus<br>für zwei Generationen<br>mit großer Photovoltaik-<br>anlage!</h3>
    <p>74417 Gschwend</p>
    Kaufpreis: 580.000,00€<br>Fläche: 280,00m²<br>Grundstück: 903,00m²<br>Zimmer: 8
  </div>
  <div class="listing-text" style="left:1022px;top:510px;width:140px">
    <p>Energieausweis:<br>Energieeffizenzklasse E</p><p>Energieausweistyp:<br>Bedarfsausweis</p>Energiebedarf/<br>Energieverbrauch:<br>140 kWh/(m²*a)
  </div>

  <div class="listing-frame" style="left:637px;top:672px;width:353px;height:158px"></div>
  <div class="photo" role="img" aria-label="Weißes Mehrfamilienhaus mit Praxisanbau" style="left:953px;top:681px;width:212px;height:141px;background:linear-gradient(180deg,#8fb6dd 0%,#bcd3e8 35%,#e9ebee 50%,#c8ccd2 75%,#8e8f8c 100%)"></div>
  <div class="listing-text" style="left:668px;top:696px;width:145px">
    <h3>Mehrfamilienhaus mit<br>Praxiseinheit<br>Lukrative Kapitalanlage</h3>
    <p>74405 Gaildorf</p>
    Kaufpreis: 369.000,00€<br>Fläche: 241,00m²<br>Grundstück: 1.018,00m²<br>Zimmer: 16
  </div>
  <div class="listing-text" style="left:818px;top:696px;width:130px">
    <p>Energieausweis:<br>Energieeffizienzklasse F</p><p>Energieausweistyp:<br>Verbrauchsausweis</p>Energiebedarf/<br>Energieverbrauch:<br>175kWh/(m²*a)
  </div>

</main>
</body>
</html>
```